New Business Card Design Project VORALDI-Italy

we are VORALDI-Italy
our company in the market for 3 years we are luxury cosmetic company and its about time for a facelift :)
i will like to have elegant luxurious and unique business card
that will give the person that get it a unique, luxurious and elegant impression
I'm VERY OPEN FOR NEW IDEAS , even duo i add a few files of things that i see on line and i like them

i add my logo as well
my website is VORALDI.COM
(if you would like to see the main style that we have)

Target Market(s)

adult that have money :)

Industry/Entity Type

Business

Contact Information for Business Card

Name - Paul Voraldi
Position - CEO and CO Founder
address - 4718 E Danbury
telephone - 555-318-4402
email - paul@voraldi-example.com
fax - 555-318-4402
website - VORALDI.COM

Colors
000000
959595
fbee3e
ffffff

Requirements
Must have
• big logo in GOLD color
• elegant look
• impressive
Nice to have
• not must but maybe classy pattern background
• not must but maybe emblem
• maybe clear plastic business card
Should not have
• colors
• images

```html
<!DOCTYPE html>
<html lang="en">
<head>
<meta charset="utf-8">
<title>VORALDI-Italy Business Card</title>
<link rel="stylesheet" href="https://fonts.googleapis.com/css2?family=Open+Sans:wght@400;600&display=swap">
<style>
  :root {
    --backdrop: #2a2a2c;
    --paper: #fbfbfa;
    --gold: #c9a232;
    --gold-light: #dcbd55;
    --gold-deep: #bf962a;
    --ink: #4a4a4a;
    --white: #ffffff;
  }
  * { margin: 0; padding: 0; box-sizing: border-box; }
  html, body {
    width: 1200px;
    height: 960px;
    overflow: hidden;
    background: var(--backdrop);
    font-family: "Open Sans", Arial, sans-serif;
  }
  .canvas {
    position: relative;
    width: 1200px;
    height: 960px;
  }
  .card {
    position: absolute;
    left: 250px;
    width: 700px;
    height: 400px;
    border-radius: 4px;
    box-shadow: 0 14px 30px rgba(0,0,0,0.45);
  }
  /* Back side */
  .card--back {
    top: 53px;
    background: linear-gradient(160deg, var(--gold-light) 0%, var(--gold) 55%, var(--gold-deep) 100%);
    display: flex;
    flex-direction: column;
    align-items: center;
    justify-content: center;
    color: var(--white);
  }
  /* Front side */
  .card--front {
    top: 507px;
    background: var(--paper);
    display: flex;
    align-items: center;
  }
  /* Brand block */
  .brand {
    display: flex;
    flex-direction: column;
    align-items: center;
    font-weight: 400;
  }
  .brand__seal {
    width: 74px;
    height: 74px;
    border-radius: 50%;
    border: 3px solid currentColor;
    margin-bottom: 16px;
  }
  .brand__name {
    font-size: 46px;
    letter-spacing: 3px;
    line-height: 1;
  }
  .brand__rule {
    width: 240px;
    height: 2px;
    background: currentColor;
    margin: 10px 0 8px;
  }
  .brand__region {
    font-size: 15px;
    letter-spacing: 3px;
    line-height: 1;
  }
  .card--back .brand { color: var(--white); opacity: 0.9; }
  .back__web {
    margin-top: 26px;
    font-size: 16px;
    letter-spacing: 5px;
    color: var(--white);
    opacity: 0.85;
  }
  .front__brand {
    width: 345px;
    color: var(--gold);
  }
  .front__divider {
    width: 2px;
    height: 200px;
    background: var(--gold);
  }
  .contact {
    padding-left: 30px;
    color: var(--ink);
    font-size: 16px;
    line-height: 1.35;
  }
  .contact__name {
    color: var(--gold);
    font-weight: 600;
    font-size: 22px;
    line-height: 1.2;
  }
  .contact__role {
    font-size: 18px;
    margin-bottom: 16px;
  }
  .contact__address { margin-bottom: 8px; }
</style>
</head>
<body>
<main class="canvas">

  <section class="card card--back" aria-label="Card back">
    <div class="brand">
      <span class="brand__seal"></span>
      <span class="brand__name">VORALDI</span>
      <span class="brand__rule"></span>
      <span class="brand__region">ITALY</span>
    </div>
    <p class="back__web">www.voraldi.com</p>
  </section>

  <section class="card card--front" aria-label="Card front">
    <div class="brand front__brand">
      <span class="brand__seal"></span>
      <span class="brand__name">VORALDI</span>
      <span class="brand__rule"></span>
      <span class="brand__region">ITALY</span>
    </div>
    <span class="front__divider"></span>
    <div class="contact">
      <p class="contact__name">Paul Voraldi</p>
      <p class="contact__role">CEO &amp; CO Founder</p>
      <p class="contact__address">4718 E Danbury</p>
      <p>P. 555-318-4402</p>
      <p>F. 555-318-4402</p>
      <p>E. paul@voraldi-example.com</p>
      <p>W. VORALDI.COM</p>
    </div>
  </section>

</main>
</body>
</html>
```